Re-design of our website - Property Development Company

Our current website is now old and stale. We are looking for a Wordpress design for a new website. Our company is a property development and property investment company. We have different projects that are under construction and have completed a number also. We would like to showcase these projects as individual pages. The projects are located all over the east coast of Australia and a mixture of retail, industrial, residential subdivsions. In the near future we are hoping to start a small property funds management division as well.

Current website is www.korvanith.com.au

We are wanting you to design a page for the each of following (total of 3 pages):
- Home page
- Project page (which will be used to showcase each development project). There are 4 active projects that we currently own and a number of completed projects.
- Information page (which will be used for about us, contact us, management etc.)

Feel free to go out of the box and wow us. We are open to new ideas.
Updates

Reason: Hi I am going on annual leave for a week being 17-21 Feb so wont be able to comment on anyones design so I have given you an extra week and a bit to finish off your 3 pages. Thanks for the designs so far, they are looking good.

Target Market(s)

It will be used by business professionals researching our company including:
- current investors
- new investors
- consultants (architects, builders, town planners, council, real estate managers/agents, engineers etc.)
- Bank lenders

We want these people to think yes we want to work with this company, they look like they are exceptional at what they do, professional, highly capable.

Industry/Entity Type

Investment

Requirements
Must have
• Our Logo. Files attached. This can be modified if you think it needs to be improved.
Nice to have
• We like clean looking websites.
• We will have some professional photographs taken of our current property developments once they are completed - two shopping centres that will be our signature developments to date. For the time being I have uploaded some aerial photographs on one of our projects under construction and also some nice photos of one of our completed developments. This should help with designing the project page.
Should not have
• We don't like busy websites with too much going on and you don't know what to look at.

```html
<!DOCTYPE html>
<html lang="en">
<head>
<meta charset="utf-8">
<title>Korvanith Partners — Home</title>
<link href="https://fonts.googleapis.com/css2?family=Open+Sans:wght@400;600;700&family=PT+Sans:wght@400;700&family=PT+Sans+Narrow:wght@400;700&display=swap" rel="stylesheet">
<style>
:root{
  --brand-blue:#2f5fb3;
  --band-blue:#3a63ad;
  --ink:#333;
  --muted:#777;
  --light-bg:#f2f2f2;
  --line:#dcdcdc;
  --white:#fff;
  --hero-dark:#5a6058;
  --hero-light:#9aa39a;
}
*{box-sizing:border-box;margin:0;padding:0}
html,body{width:989px;height:1200px;overflow:hidden;background:var(--white)}
body{font-family:"Open Sans",Arial,sans-serif;color:var(--ink);position:relative}
.site-header{position:absolute;top:0;left:0;width:989px;height:82px;background:var(--white)}
.brand{position:absolute;left:56px;top:26px;display:flex;align-items:center;gap:8px;font-family:"PT Sans",Arial,sans-serif;font-weight:700;font-size:19px;color:var(--brand-blue)}
.brand-mark{width:14px;height:14px;background:var(--brand-blue)}
.partner-login{position:absolute;right:65px;top:11px;font-size:9px;color:#555;display:flex;align-items:center;gap:5px}
.main-nav{position:absolute;top:49px;left:0;width:989px;font-family:"PT Sans Narrow",Arial,sans-serif;font-size:13px;color:#444}
.main-nav a{position:absolute;text-decoration:none;color:inherit;white-space:nowrap}
.main-nav a.is-current{color:var(--brand-blue)}
.hero{position:absolute;top:82px;left:0;width:989px;height:530px;background:radial-gradient(ellipse at 50% 45%,#d8dbd6 0%,#9ca39b 35%,#5c655a 70%,#3f4a3b 100%)}
.hero-title{position:absolute;top:222px;width:100%;text-align:center;font-family:"PT Sans",Arial,sans-serif;font-weight:700;font-size:35px;letter-spacing:1px;color:var(--white)}
.intro-band{position:absolute;top:612px;left:0;width:989px;height:78px;background:var(--band-blue);color:var(--white);font-size:11.6px;line-height:15.5px;padding:15px 74px 0}
.about{position:absolute;top:690px;left:0;width:989px;height:222px}
.about-text{position:absolute;left:56px;top:28px;width:520px;font-size:10.6px;line-height:20px;color:var(--muted)}
.about-text p+p{margin-top:10px}
.about-text .name{color:var(--brand-blue)}
.about-photo{position:absolute;left:616px;top:21px;width:309px;height:140px;background:linear-gradient(100deg,#c7483b 0%,#a8403a 35%,#6f6a66 60%,#9aa0a4 100%)}
.site-footer{position:absolute;top:912px;left:0;width:989px;height:233px;background:var(--light-bg)}
.ask{position:absolute;top:13px;width:100%;text-align:center;font-size:20px;color:var(--brand-blue)}
.social{position:absolute;right:66px;top:17px;display:flex;gap:14px}
.social span{width:15px;height:15px;border-radius:50%;background:var(--brand-blue)}
.footer-rule{position:absolute;top:46px;left:0;width:100%;height:1px;background:var(--line)}
.col-title{font-size:10.5px;font-weight:600;color:var(--brand-blue);margin-bottom:8px}
.tweets{position:absolute;left:51px;top:54px;width:150px}
.tweet{font-size:7.5px;line-height:10.5px;color:#444;padding-bottom:7px;margin-bottom:7px;border-bottom:1px solid var(--line)}
.tweet b{font-weight:700}
.tweet em{display:block;color:#666}
.posts{position:absolute;left:259px;top:57px;width:320px}
.post-grid{display:grid;grid-template-columns:150px 150px;column-gap:14px}
.post{font-size:7.5px;line-height:10.5px;color:#444;padding-bottom:6px;margin-bottom:7px;border-bottom:1px solid var(--line)}
.post strong{display:block;font-weight:700}
.contact{position:absolute;left:649px;top:54px;width:262px}
.contact label{display:block;font-size:7.8px;color:#333;margin-bottom:3px}
.field-row{display:flex;gap:5px}
.field-row div{flex:1}
.field{background:var(--white);height:24px;margin-bottom:8px}
.field.tall{height:46px}
.captcha-row{display:flex;align-items:center;gap:14px;margin-top:2px}
.captcha{font-size:11px;letter-spacing:3px;font-weight:700;color:#555;width:44px}
.captcha-input{width:64px;height:24px;background:var(--white)}
.send{margin-left:auto;background:var(--brand-blue);color:var(--white);font-size:11px;width:103px;height:25px;display:flex;align-items:center;justify-content:center}
.base{position:absolute;top:1145px;left:0;width:989px;height:55px;font-size:7.3px;color:#444}
.base .links{position:absolute;left:45px;top:11px}
.base .copy{position:absolute;left:45px;top:30px}
.base .mini-brand{position:absolute;right:66px;top:12px;display:flex;align-items:center;gap:4px;font-family:"PT Sans",Arial,sans-serif;font-weight:700;font-size:9px;color:#888}
.base .mini-brand i{width:7px;height:7px;background:#888}
</style>
</head>
<body>
<header class="site-header">
  <div class="brand"><span class="brand-mark"></span>Korvanith Partners</div>
  <div class="partner-login">
    <svg width="8" height="9" viewBox="0 0 8 9"><circle cx="4" cy="2.3" r="2.1" fill="#555"/><path d="M0 9c0-3 1.8-4.3 4-4.3S8 6 8 9z" fill="#555"/></svg>
    Partner Login
  </div>
  <nav class="main-nav">
    <a class="is-current" href="#" style="left:505px">Home</a>
    <a href="#" style="left:578px">Philosophy</a>
    <a href="#" style="left:667px">Activities &amp; Projects</a>
    <a href="#" style="left:782px">Management</a>
    <a href="#" style="left:873px">File Upload</a>
  </nav>
</header>

<section class="hero" role="img" aria-label="Aerial photograph of a large white-roofed retail development under construction">
  <h1 class="hero-title">SUCCESS THROUGH DISCIPLINE</h1>
</section>

<section class="intro-band">
  <p>Having started operations in 2001, Korvanith Partners is an established “value add” property group with a focus on property development.</p>
  <p>Korvanith Partners is an opportunistic total return investor / developer with the proven capability to successfully identify, acquire, manage and deliver property projects that are anticipated to deliver strong returns to our group and partners.</p>
</section>

<section class="about">
  <div class="about-text">
    <p><span class="name">Korvanith Partners</span> is an opportunistic total return investor / developer with the proven capability to successfully identify, acquire, manage and deliver property projects that are anticipated to deliver strong returns to our group and partners.</p>
    <p>Through the projects we have created and participated in over the years, Korvanith Partners has refined substantial skill sets in the areas of bulky goods, retail, industrial and commercial development.</p>
  </div>
  <div class="about-photo" role="img" aria-label="Photograph of shoppers outside a red shopfront at a completed retail development"></div>
</section>

<footer class="site-footer">
  <div class="ask">Questions? Just Ask 1-800-555-0142</div>
  <div class="social" aria-label="Social links"><span></span><span></span><span></span></div>
  <div class="footer-rule"></div>

  <div class="tweets">
    <h3 class="col-title">Latest Tweets</h3>
    <div class="tweet">RT <b>@korvnews</b>: Duis autem vel eum iriure dolor in hendrerit in vulputate velit esse molestie consequat n vulputate velit...<em>3 days ago</em></div>
    <div class="tweet">RT <b>@korvnews</b>: Duis autem vel eum iriure dolor in hendrerit in vulputate velit esse molestie consequat n vulputate velit...<em>3 days ago</em></div>
    <div class="tweet">RT <b>@korvnews</b>: Duis autem vel eum iriure dolor in hendrerit in vulputate velit esse molestie consequat n vulputate velit...<em>3 days ago</em></div>
  </div>

  <div class="posts">
    <h3 class="col-title">Recent Posts</h3>
    <div class="post-grid">
      <div class="post"><strong>Myblog</strong>Back Up Now or be sorry later. Maintaining an up-to-date backup file can save...</div>
      <div class="post"><strong>Myblog</strong>Back Up Now or be sorry later. Maintaining an up-to-date backup file can save...</div>
      <div class="post"><strong>Myblog</strong>Back Up Now or be sorry later. Maintaining an up-to-date backup file can save...</div>
      <div class="post"><strong>Myblog</strong>Back Up Now or be sorry later. Maintaining an up-to-date backup file can save...</div>
      <div class="post"><strong>Myblog</strong>Back Up Now or be sorry later. Maintaining an up-to-date backup file can save...</div>
      <div class="post"><strong>Myblog</strong>Back Up Now or be sorry later. Maintaining an up-to-date backup file can save...</div>
    </div>
  </div>

  <div class="contact">
    <h3 class="col-title">Get in Touch</h3>
    <div class="field-row">
      <div><label>Your Name (required)</label><div class="field"></div></div>
      <div><label>Email (required)</label><div class="field"></div></div>
    </div>
    <label>Message</label>
    <div class="field tall"></div>
    <div class="captcha-row">
      <span class="captcha">9K6N</span>
      <span class="captcha-input"></span>
      <span class="send">Send Message</span>
    </div>
  </div>
</footer>

<div class="base">
  <div class="links">Site Terms &amp; Conditions | &nbsp;Sitemap &nbsp;| &nbsp;Policy</div>
  <div class="copy">Korvanith Partners ©2014. All rights reserved.</div>
  <div class="mini-brand"><i></i>Korvanith</div>
</div>
</body>
</html>
```